Real Estate Flyer (Brenton Property)

We need a color CMYK high resolution, print quality horizontal real estate property flyer designed in the sizes of 10" wide and 6.7425" tall and another one in 11" wide and 8.5" tall.
Ad should be professionally looking to U.S. standards. It should be sleek, modern yet classy.
We uploaded in Briefs logo files, agent photo, 2 photos of the property (Must use both) and a sample of a flyer for Vayle Morrow Luxury Residence. We like how the overlay atop the first photo in the Vayle Morrow flyer with the company logo in the overlay. We'd like to incorporate that with our logo, the background color of the overlay should match that of our logo. DON'T CHANGE LOGO COLORS. Only use two colors in ad (exact logo blue color and white). The text in the overlay must be "FOR SALE - Potential Income Producing Commercial Office Building". Other details that should be prominent underneath are "42 Brenton Dr., Schaumburg, IL 60174 - Asking Price: $650,000".
Add "Residential & Commercial" under our company logo in italic font.
Add in flyer: "Located seconds away from the Kettering Rd. & Palden Rd. Intersection"
Add in flyer:
- Completely vacant
- 10,000 sq. ft. building
- 55 Car Parking
- 1.38 acre lot
- Over 20 offices and 5 bathrooms.
- Lease out individual office spaces for great monthly cash flow
Put agent's photo and following details professionally displayed:
Dev Marlo
Managing Broker
847-555-0148
dev.marlo@qtnhomes-example.com
Add from Briefs fair housing logo and PLX logo near agent's information. Logos should be small but yet visible to understand text.
Add at bottom of the ad with separation near agent details:
Looking to Buy or Sell?
I’m your one-stop, full service licensed real estate broker.
I deal with all types of real estate properties: Homes, Condos, Townhomes, Multi-Unit Apartment Buildings and Commercial Spaces.
Let My Experience Guide You Through Every Step of the Process!
Fine print:
©2018 QTN Homes, Inc. All Rights Reserved.

```html
<!DOCTYPE html>
<html lang="en">
<head>
<meta charset="utf-8">
<title>Brenton Property – For Sale Flyer</title>
<link rel="stylesheet" href="https://fonts.googleapis.com/css2?family=Montserrat:wght@400;500;700&family=Roboto+Condensed:wght@400;700&display=swap">
<style>
  :root {
    --brand-blue: #2d55a8;
    --overlay-blue: rgba(40, 78, 160, 0.88);
    --bar-blue: #1f8ccc;
    --agent-blue: #1a9ad8;
    --title-blue: #1f4a9e;
    --rule-blue: #3f7fc4;
    --ink: #222831;
    --grey: #4a4f57;
    --white: #ffffff;
    --stage: #e8eaee;
  }
  * { box-sizing: border-box; margin: 0; padding: 0; }
  html, body { width: 1200px; height: 1200px; overflow: hidden; background: var(--stage); }
  body { font-family: "Montserrat", sans-serif; color: var(--ink); position: relative; }

  .flyer { position: absolute; left: 0; top: 137px; width: 1200px; height: 926px; background: var(--white); overflow: hidden; }
  .abs { position: absolute; }

  .hero-photo { left: 0; top: 0; width: 823px; height: 563px;
    background: linear-gradient(180deg, #8fa3bf 0%, #c9b59a 35%, #a8845e 55%, #4d4a47 80%, #3a3d44 100%); }
  .hero-overlay { left: 0; top: 370px; width: 823px; height: 134px; background: var(--overlay-blue); }
  .for-sale { left: 42px; top: 392px; color: var(--white); font-weight: 700; font-size: 52px; line-height: 44px; letter-spacing: 1px; }
  .headline { left: 228px; top: 390px; color: var(--white); font-weight: 400; font-size: 40px; line-height: 48px; letter-spacing: 0.5px; white-space: nowrap; }
  .address-bar { left: 0; top: 504px; width: 823px; height: 59px; background: var(--bar-blue); color: var(--white);
    font-size: 24px; line-height: 59px; padding-left: 42px; white-space: nowrap; }

  .brand-box { left: 598px; top: 0; width: 178px; height: 135px; background: var(--brand-blue);
    display: flex; align-items: center; justify-content: center; gap: 8px; color: var(--white);
    font-weight: 700; font-size: 22px; white-space: nowrap; }
  .brand-box .mark { width: 12px; height: 12px; background: var(--white); flex: none; }
  .brand-tag { right: 424px; top: 142px; text-align: right; font-style: italic; font-weight: 700; font-size: 13px;
    color: var(--title-blue); white-space: nowrap; }

  .location { left: 42px; top: 602px; font-weight: 700; font-size: 30px; line-height: 36px; color: var(--ink); white-space: nowrap; }
  .rule { left: 42px; width: 872px; height: 2px; background: var(--rule-blue); }
  .rule.top { top: 695px; }
  .rule.bottom { top: 891px; }
  .divider { top: 724px; width: 2px; height: 142px; background: var(--rule-blue); }

  .stat .small { font-size: 18px; color: var(--grey); line-height: 20px; }
  .stat .big { font-weight: 700; font-size: 38px; color: var(--title-blue); line-height: 40px; }
  .stat .huge { font-weight: 700; font-size: 50px; color: var(--title-blue); line-height: 52px; }
  .stat .label { font-weight: 700; font-size: 18px; color: var(--title-blue); line-height: 20px; }
  .stat .faded { color: #9aa8bf; }
  .lease { left: 645px; top: 726px; font-size: 18px; line-height: 25px; color: var(--title-blue); }
  .lease b { font-weight: 700; }

  .side-photo-a { left: 827px; top: 0; width: 373px; height: 280px;
    background: linear-gradient(180deg, #9eb0c6 0%, #c8b596 45%, #3f4248 75%, #2e3035 100%); }
  .side-photo-b { left: 827px; top: 283px; width: 373px; height: 280px;
    background: linear-gradient(180deg, #aab8c9 0%, #8a8872 40%, #3c3f45 65%, #2c2e33 100%); }
  .side-stat { left: 851px; color: var(--white); }
  .side-stat .num { font-weight: 700; font-size: 50px; line-height: 52px; }
  .side-stat .sub { font-size: 25px; line-height: 28px; }
  .parking { left: 851px; top: 508px; color: var(--white); display: flex; align-items: center; gap: 8px; }
  .parking .num { font-weight: 700; font-size: 50px; line-height: 50px; }
  .parking .sub { font-size: 25px; line-height: 21px; }

  .agent-photo { left: 827px; top: 563px; width: 140px; height: 173px; background: linear-gradient(180deg, #f2f2f2 0%, #c9c2bb 55%, #2a2c31 100%); }
  .agent-card { left: 967px; top: 563px; width: 233px; height: 173px; background: var(--agent-blue); color: var(--white); padding: 10px 0 0 18px; }
  .agent-card .name { font-weight: 700; font-size: 20px; line-height: 22px; }
  .agent-card .role { font-size: 14px; line-height: 16px; opacity: 0.9; }
  .agent-card .phone { font-weight: 700; font-size: 20px; line-height: 24px; margin-top: 10px; }
  .agent-card .email { font-size: 11.5px; line-height: 16px; margin-top: 4px; white-space: nowrap; letter-spacing: -0.1px; }
  .badges { display: flex; gap: 12px; margin-top: 12px; align-items: flex-end; }
  .badge-square { width: 38px; height: 38px; background: var(--white); }
  .badge-wide { width: 74px; height: 38px; background: var(--white); }

  .pitch { left: 827px; top: 736px; width: 373px; height: 190px; background: var(--brand-blue); color: var(--white); padding: 12px 22px 0 24px; }
  .pitch h2 { font-weight: 400; font-size: 27px; line-height: 32px; white-space: nowrap; }
  .pitch p { font-family: "Roboto Condensed", sans-serif; font-weight: 700; font-size: 12px; line-height: 17px; margin-top: 5px; }
  .pitch .fine { font-family: "Roboto Condensed", sans-serif; font-size: 11.5px; line-height: 14px; margin-top: 12px; }
</style>
</head>
<body>
<main class="flyer">
  <div class="abs hero-photo" role="img" aria-label="Photo of the two-storey commercial office building with dormer windows at sunset"></div>
  <div class="abs hero-overlay"></div>
  <div class="abs for-sale">FOR<br>SALE</div>
  <div class="abs headline">Potential Income Producing<br>Commercial Office Building</div>
  <div class="abs address-bar">42 Brenton Dr., Schaumburg, IL 60174 - Asking Price: $650,000</div>

  <div class="abs brand-box"><span class="mark"></span>QTN Homes</div>
  <div class="abs brand-tag">Residential &amp; Commercial</div>

  <div class="abs location">Located seconds away from the Kettering Rd.<br>&amp; Palden Rd. Intersection</div>
  <div class="abs rule top"></div>

  <div class="abs stat" style="left:42px; top:724px;">
    <div class="small">Completely</div>
    <div class="big" style="font-size:36px; line-height:34px;">Vacant</div>
    <div class="huge" style="margin-top:12px;">1.38</div>
    <div class="small">Acre Lot</div>
  </div>
  <div class="abs divider" style="left:207px;"></div>

  <div class="abs stat" style="left:253px; top:734px;">
    <div class="big">10,000</div>
    <div class="small">sq. ft. Building</div>
    <div class="big" style="margin-top:28px;">55</div>
    <div class="small">Car Parking</div>
  </div>
  <div class="abs divider" style="left:433px;"></div>

  <div class="abs stat" style="left:469px; top:724px;">
    <div class="small">Over</div>
    <div class="big">20</div>
    <div class="label">Offices</div>
    <div class="big" style="margin-top:6px;"><span class="faded">&amp;</span>5</div>
    <div class="label">Bathrooms</div>
  </div>
  <div class="abs divider" style="left:605px;"></div>

  <div class="abs lease"><b>Lease out</b><br>individual<br><b>office spaces</b><br><b>for great</b><br><b>monthly</b><br><b>cash flow</b></div>
  <div class="abs rule bottom"></div>

  <div class="abs side-photo-a" role="img" aria-label="Photo of the building exterior and front parking lot"></div>
  <div class="abs side-stat" style="top:175px;">
    <div class="num">10,000</div>
    <div class="sub">sq. ft. building</div>
  </div>
  <div class="abs side-photo-b" role="img" aria-label="Photo of the parking lot with marked spaces"></div>
  <div class="abs parking"><span class="num">55</span><span class="sub">Car<br>Parking</span></div>

  <div class="abs agent-photo" role="img" aria-label="Portrait of the managing broker"></div>
  <div class="abs agent-card">
    <div class="name">Dev Marlo</div>
    <div class="role">Managing Broker</div>
    <div class="phone">847-555-0148</div>
    <div class="email">dev.marlo@qtnhomes-example.com</div>
    <div class="badges"><span class="badge-square"></span><span class="badge-wide"></span></div>
  </div>

  <section class="abs pitch">
    <h2>Looking to Buy or Sell?</h2>
    <p>I’m your one-stop, full service licensed real estate broker. I deal with all types of real estate properties: Homes, Condos, Townhomes, Multi-Unit Apartment Buildings and Commercial Spaces. Let My Experience Guide You Through Every Step of the Process!</p>
    <div class="fine">©2018 QTN Homes, Inc. All Rights Reserved.</div>
  </section>
</main>
</body>
</html>
```